Web Page Design (Coded). Winner can expect additional work to implement

My current employer (www.harbinfield.com.au) requires the establishment of a new web page (www.harbinbluetorch.com.au) to promote safety and environmental products which will be sold to the oil / gas / mining and environmental sectors. The web page needs to be somehow aligned with the parent company page above (if only the colouring to appease my boss), yet innovate and awesome. The successful designer will be expected to provide coded files and be able to provide additional services to edit and launch the website. The website is currently operational but the content and format are both poor. The website will be predominantly based around promoting our products but will include a "buy online" section for some products which will be part of the website, but on a different tab / layer. Video's and flash will be part of the successful web page. Actually, I know very little about web pages so just go for gold and make it good and make it work. I am not adding any files at this point in time, but do post a message if you require any files.

Target Market(s)

Our products will be promoted to customers in Australia and SE Asia in the mining, oil and gas sectors predominantly with local government also a purchaser. Most purchase decisions will be made by males and people needing to solve problems quickly. They often won't care what product they receive as long as it does the job.

Industry/Entity Type

Safety

Requirements
Must have
• Must be aligned with our parent company page design (www.harbinfield.com.au). When I say aligned, I am talking effectively about fonts and colouring. The page design itself can be innovative beyond the parent company page design.
Somewhere on the page it must say we are a division of Harbinfield Pty Ltd.
Nice to have
• Easy to find products, read about them and download brochures. Links to be provided to "buy online" or "request a quote" next to each product, but without pricing.
It is essential that contacting us by phone, email etc... is easy to find through every layer of the page. This is essential. We would like some photo's on the home page scrolling through products, but these do not need to be large. Our current website (harbinbluetorch.com.au) has photo's but they are too big.

```html
<!DOCTYPE html>
<html lang="en">
<head>
<meta charset="utf-8">
<title>Harbin Blue Torch – Distributor of Disaster Management Technologies</title>
<link rel="stylesheet" href="https://fonts.googleapis.com/css2?family=Raleway:wght@300;400;500;600;700;800&display=swap">
<style>
  :root{
    --gold:#f5b11b;
    --gold-dark:#e29d0a;
    --navy:#16204f;
    --navy-deep:#0d1430;
    --ink:#3d3d3d;
    --muted:#7a7a7a;
    --paper:#ffffff;
    --mist:#f3f4f7;
    --line:#e3e5ea;
  }
  *{box-sizing:border-box;margin:0;padding:0}
  html,body{width:728px;height:1200px;overflow:hidden;background:var(--paper)}
  body{font-family:'Raleway',Arial,sans-serif;color:var(--ink);position:relative}
  .page{position:relative;width:728px;height:1200px;overflow:hidden}

  /* header */
  .site-header{position:absolute;left:0;top:0;width:728px;height:36px;background:var(--paper);border-bottom:1px solid var(--line)}
  .brand{position:absolute;left:122px;top:5px;line-height:1}
  .brand-name{font-weight:800;font-size:16px;color:var(--navy);letter-spacing:-.2px}
  .brand-sub{font-weight:800;font-size:7px;color:var(--navy);letter-spacing:.6px;margin-top:2px}
  .main-nav{position:absolute;left:272px;top:13px;display:flex;gap:8px;font-size:6.6px;text-transform:uppercase;color:#6b6b6b}
  .main-nav a{color:inherit;text-decoration:none;position:relative}
  .main-nav a.active{color:var(--gold)}
  .main-nav a.active:after{content:"";position:absolute;left:0;right:0;top:21px;height:2px;background:var(--gold)}
  .social-top{position:absolute;left:482px;top:12px;display:flex;gap:3px}
  .social-top span{width:10px;height:10px;border-radius:50%;background:var(--gold)}
  .search{position:absolute;left:527px;top:10px;width:80px;height:16px;border:1px solid var(--gold);font-size:6px;color:var(--gold);padding:4px 5px}
  .search svg{position:absolute;right:4px;top:3px}

  /* hero */
  .hero{position:absolute;left:0;top:36px;width:728px;height:233px;background:linear-gradient(180deg,#8ea3b6 0%,#6d8aa6 22%,#3f6b92 45%,#2f5d87 100%)}
  .hero-camera{position:absolute;left:180px;top:46px;width:180px;height:187px;background:linear-gradient(180deg,#e8e8e6,#b9bcbe);border-radius:40px 40px 0 0;opacity:.85}
  .hero-title{position:absolute;left:344px;top:94px;color:#fff;line-height:1}
  .hero-title h1{font-weight:500;font-size:24px;letter-spacing:.3px}
  .hero-title p{font-weight:500;font-size:12px;margin-top:2px;text-transform:uppercase}
  .btn{display:block;background:var(--gold);color:#fff;text-transform:uppercase;font-weight:500;text-align:center;text-decoration:none}
  .hero .btn{position:absolute;left:346px;top:139px;width:108px;height:25px;line-height:25px;font-size:7.4px}

  /* welcome */
  .welcome{position:absolute;left:0;top:269px;width:728px;height:201px;background:linear-gradient(180deg,#fff 50%,#eef4ec 100%)}
  .welcome-kicker{position:absolute;left:122px;top:17px;font-size:8px;color:var(--gold);font-weight:400}
  .welcome h2{position:absolute;left:122px;top:26px;font-size:15px;font-weight:400;color:#333}
  .welcome-copy{position:absolute;left:122px;top:52px;width:228px;font-size:5.6px;line-height:10.2px;color:var(--muted)}
  .welcome-copy p+p{margin-top:10px}
  .welcome .btn{position:absolute;left:122px;top:165px;width:100px;height:19px;line-height:19px;font-size:6.8px}
  .team-photo{position:absolute;left:364px;top:7px;width:244px;height:194px;background:linear-gradient(180deg,#f0ede8,#c9c3b9 55%,#6d6e73);border-radius:60px 60px 0 0}
  .help-box{position:absolute;left:422px;top:123px;width:148px;height:63px;background:var(--gold);color:#fff;padding:10px 11px}
  .help-box h3{font-size:6.6px;font-weight:500}
  .help-box p{font-size:5.2px;line-height:7px;margin-top:4px}
  .help-phone{display:flex;align-items:center;justify-content:center;gap:4px;font-size:9.5px;font-weight:500;margin-top:7px}

  /* products */
  .products{position:absolute;left:0;top:470px;width:728px;height:231px;background:var(--navy);color:#fff;text-align:center}
  .section-title{font-size:17px;font-weight:300}
  .products .section-title{margin-top:16px}
  .section-sub{font-size:7.2px;line-height:9px;width:300px;margin:5px auto 0}
  .products .section-sub{color:#b7bcd3}
  .product-card{position:absolute;top:79px;width:107px}
  .product-card .thumb{width:107px;height:59px}
  .product-card h3{font-size:8px;color:var(--gold);font-weight:500;margin-top:9px}
  .product-card p{font-size:5.6px;line-height:8px;color:#dfe2ee;margin-top:2px}
  .product-card .btn{width:61px;height:16px;line-height:16px;font-size:6.4px;margin:6px auto 0}

  /* sectors */
  .sectors{position:absolute;left:0;top:701px;width:728px;height:151px;background:var(--mist);text-align:center}
  .sectors .section-title{margin-top:16px;color:#333}
  .sectors .section-sub{color:var(--gold)}
  .sector{position:absolute;top:81px;width:160px;text-align:left}
  .sector-icon{position:absolute;left:0;top:0;width:51px;height:51px;border-radius:50%;background:#fff;border:2px solid #e0e0e0;display:flex;align-items:center;justify-content:center}
  .sector h3{position:absolute;left:58px;top:5px;font-size:9.4px;font-weight:500;color:#333;white-space:nowrap}
  .sector p{position:absolute;left:58px;top:18px;width:92px;font-size:5.6px;line-height:8px;color:var(--muted)}

  /* testimonials */
  .testimonials{position:absolute;left:0;top:852px;width:728px;height:164px;background:var(--paper);text-align:center}
  .testimonials .section-title{margin-top:11px;color:#333}
  .rating{display:flex;align-items:center;justify-content:center;gap:1px;margin-top:3px;font-size:6px;color:var(--gold)}
  .rating b{font-weight:400;margin-left:3px}
  .quote-card{position:absolute;top:60px;width:234px;height:67px;background:var(--mist);border:1px solid var(--line);text-align:left}
  .avatar{position:absolute;left:12px;top:11px;width:48px;height:40px;border-radius:50%;background:linear-gradient(135deg,#e6d3bf,#b98d6a)}
  .quote-card p{position:absolute;left:72px;top:11px;width:150px;font-size:5.6px;line-height:8.8px;color:#555}
  .quote-card .author{position:absolute;left:72px;top:51px;font-size:5px;color:var(--navy);font-weight:600}
  .dots{position:absolute;left:356px;top:146px;display:flex;gap:1.5px}
  .dots span{width:2.5px;height:2.5px;border-radius:50%;background:#ccc}
  .dots span.on{background:#888}

  /* partners */
  .partners{position:absolute;left:0;top:1016px;width:728px;height:68px;background:var(--mist);text-align:center}
  .partners h2{font-size:7.8px;font-weight:500;color:#444;margin-top:14px}
  .partner-row{position:absolute;left:160px;top:34px;width:410px;display:flex;justify-content:space-between;align-items:center;font-weight:700;font-size:13px;color:#6b7280}

  /* footer */
  .site-footer{position:absolute;left:0;top:1084px;width:728px;height:116px;background:var(--navy-deep);color:#fff}
  .footer-col{position:absolute;top:23px}
  .footer-col h4{font-size:7px;font-weight:700;text-transform:uppercase}
  .footer-links{display:grid;grid-template-columns:43px 50px;row-gap:5.6px;margin-top:10px;font-size:5.2px;color:#c5c9d8}
  .footer-social{margin-top:10px;font-size:5.2px;color:#c5c9d8}
  .footer-social li{list-style:none;display:flex;align-items:center;gap:7px;height:12.6px}
  .footer-social li span{width:8px;height:8px;border-radius:50%;background:var(--gold)}
  .news{margin-top:10px;width:140px}
  .news h5{font-size:6px;color:var(--gold);font-weight:500}
  .news p{font-size:5px;line-height:7.2px;color:#c5c9d8;margin-bottom:6px}
  .divider{position:absolute;top:22px;width:1px;height:80px;background:#1e274a}
  .footer-brand{position:absolute;left:513px;top:21px;line-height:1}
  .footer-brand .brand-name{color:#fff;font-size:18px}
  .footer-brand .brand-sub{color:#fff;font-size:7.6px}
  .footer-brand small{display:block;font-size:5.2px;line-height:7.6px;color:#c5c9d8;margin-top:8px}
</style>
</head>
<body>
<div class="page">

  <header class="site-header">
    <div class="brand">
      <div class="brand-name">harbin</div>
      <div class="brand-sub">BLUE TORCH</div>
    </div>
    <nav class="main-nav">
      <a class="active" href="#">Home</a>
      <a href="#">About Us</a>
      <a href="#">Products</a>
      <a href="#">Solutions</a>
      <a href="#">Contact Us</a>
    </nav>
    <div class="social-top"><span></span><span></span><span></span></div>
    <div class="search">Search here...
      <svg width="8" height="8" viewBox="0 0 10 10"><circle cx="4" cy="4" r="3" fill="none" stroke="#f5b11b" stroke-width="1.5"/><line x1="6.2" y1="6.2" x2="9" y2="9" stroke="#f5b11b" stroke-width="1.6"/></svg>
    </div>
  </header>

  <section class="hero">
    <div class="hero-camera" role="img" aria-label="Photo of a security camera on a pole overlooking a harbour city"></div>
    <div class="hero-title">
      <h1>DISTRIBUTOR</h1>
      <p>of disaster management technologies</p>
    </div>
    <a class="btn" href="#">View Our Products</a>
  </section>

  <section class="welcome">
    <div class="welcome-kicker">Welcome to</div>
    <h2>Harbin Blue Torch</h2>
    <div class="welcome-copy">
      <p>Harbin Blue Torch provides safety related products, systems and services for the protection of people and property. Utilising world leading technologies for remote monitoring, collection of data and control of public warning infrastructure we are able to greatly improve situational awareness and help reduce the risk of injury and loss of life during emergency related events. Whether for general public warning or site specific applications we have the technology, expertise and experience to help you.</p>
      <p>The products available from Blue Torch come from highly regarded suppliers, are innovative in their designs and are suitable for a wide range of applications. They are designed for use in harsh environments and to function as intended in extreme events.</p>
    </div>
    <a class="btn" href="#">Read More</a>
    <div class="team-photo" role="img" aria-label="Photo of a smiling team of four business people"></div>
    <div class="help-box">
      <h3>Need Help?</h3>
      <p>Call one of our experts. That can be on weekdays from 9-17.00.</p>
      <div class="help-phone">
        <svg width="8" height="9" viewBox="0 0 8 9"><rect x="0.5" y="0.5" width="7" height="8" rx="1" fill="none" stroke="#fff"/><rect x="2" y="2" width="4" height="1.6" fill="#fff"/><rect x="2" y="5" width="1" height="1" fill="#fff"/><rect x="3.5" y="5" width="1" height="1" fill="#fff"/><rect x="5" y="5" width="1" height="1" fill="#fff"/><rect x="2" y="6.6" width="1" height="1" fill="#fff"/><rect x="3.5" y="6.6" width="1" height="1" fill="#fff"/><rect x="5" y="6.6" width="1" height="1" fill="#fff"/></svg>
        5555 018 260
      </div>
    </div>
  </section>

  <section class="products">
    <h2 class="section-title">Our Products and Solutions</h2>
    <p class="section-sub">Fusce pretium nunc quis porta malesuada. Mauris dui purus, volutpat vel porttitor vitae, varius a nibh.</p>

    <article class="product-card" style="left:122px">
      <div class="thumb" role="img" aria-label="Photo of a warning siren tower against blue sky" style="background:linear-gradient(90deg,#4a8fd0 35%,#2a2a2a 45%,#2a2a2a 55%,#4a8fd0 65%)"></div>
      <h3>Sirens</h3>
      <p>Lorem ipsum dolor sit amet, consec tetur adipiscing elit. Nam leo venenatis non consequat ut,</p>
      <a class="btn" href="#">View More</a>
    </article>
    <article class="product-card" style="left:247px">
      <div class="thumb" role="img" aria-label="Photo of a large yellow mining haul truck" style="background:linear-gradient(180deg,#f2f2f0 30%,#c9a21c 55%,#3b3a36 100%)"></div>
      <h3>Signage</h3>
      <p>Lorem ipsum dolor sit amet, consec tetur adipiscing elit. Nam leo venenatis non consequat ut,</p>
      <a class="btn" href="#">View More</a>
    </article>
    <article class="product-card" style="left:374px">
      <div class="thumb" role="img" aria-label="Photo of a security camera mounted under an eave" style="background:linear-gradient(180deg,#8b8079,#cfc8bf 60%,#a9a29b)"></div>
      <h3>Cameras</h3>
      <p>Lorem ipsum dolor sit amet, consec tetur adipiscing elit. Nam leo venenatis non consequat ut,</p>
      <a class="btn" href="#">View More</a>
    </article>
    <article class="product-card" style="left:499px">
      <div class="thumb" role="img" aria-label="Photo of tablets and phones showing monitoring dashboards" style="background:linear-gradient(180deg,#ffffff,#e6e8ee 60%,#bfc4cf)"></div>
      <h3>Monitoring</h3>
      <p>Lorem ipsum dolor sit amet, consec tetur adipiscing elit. Nam leo venenatis non consequat ut,</p>
      <a class="btn" href="#">View More</a>
    </article>
  </section>

  <section class="sectors">
    <h2 class="section-title">Industry Sectors</h2>
    <p class="section-sub">Fusce pretium nunc quis porta malesuada. Mauris dui purus, volutpat vel porttitor vitae, varius a nibh.</p>

    <div class="sector" style="left:120px">
      <div class="sector-icon">
        <svg width="28" height="24" viewBox="0 0 28 24"><path d="M2 6h24l-3 9H5z" fill="#f5b11b"/><circle cx="8" cy="6" r="3" fill="#f5b11b"/><circle cx="14" cy="5" r="3.5" fill="#f5b11b"/><circle cx="20" cy="6" r="3" fill="#f5b11b"/><circle cx="8" cy="19" r="3.5" fill="none" stroke="#f5b11b" stroke-width="2"/><circle cx="20" cy="19" r="3.5" fill="none" stroke="#f5b11b" stroke-width="2"/><line x1="11.5" y1="19" x2="16.5" y2="19" stroke="#f5b11b" stroke-width="2"/></svg>
      </div>
      <h3>Minig</h3>
      <p>Lorem ipsum dolor sit amet, consectetur adipiscing elit. Nam leo venenatis non consequat ut,</p>
    </div>
    <div class="sector" style="left:290px">
      <div class="sector-icon">
        <svg width="18" height="26" viewBox="0 0 18 26"><path d="M9 1C9 1 1 12 1 17a8 8 0 0 0 16 0C17 12 9 1 9 1z" fill="#f5b11b"/><path d="M12 17a3 3 0 0 1-3 3" fill="none" stroke="#fff" stroke-width="1.4"/></svg>
      </div>
      <h3>Oil and Gas</h3>
      <p>Lorem ipsum dolor sit amet, consectetur adipiscing elit. Nam leo venenatis non consequat ut,</p>
    </div>
    <div class="sector" style="left:462px">
      <div class="sector-icon">
        <svg width="28" height="24" viewBox="0 0 28 24"><path d="M14 1L2 7h24z" fill="#f5b11b"/><rect x="3" y="8" width="22" height="2" fill="#f5b11b"/><rect x="5" y="11" width="3" height="8" fill="#f5b11b"/><rect x="10" y="11" width="3" height="8" fill="#f5b11b"/><rect x="15" y="11" width="3" height="8" fill="#f5b11b"/><rect x="20" y="11" width="3" height="8" fill="#f5b11b"/><rect x="2" y="20" width="24" height="3" fill="#f5b11b"/></svg>
      </div>
      <h3>Local Government</h3>
      <p>Lorem ipsum dolor sit amet, consectetur adipiscing elit. Nam leo venenatis non consequat ut,</p>
    </div>
  </section>

  <section class="testimonials">
    <h2 class="section-title">Testimonials</h2>
    <div class="rating">
      <svg width="44" height="8" viewBox="0 0 55 10">
        <g fill="#f5b11b">
          <polygon points="5,0 6.2,3.6 10,3.6 7,5.9 8.1,9.5 5,7.3 1.9,9.5 3,5.9 0,3.6 3.8,3.6"/>
          <polygon transform="translate(11 0)" points="5,0 6.2,3.6 10,3.6 7,5.9 8.1,9.5 5,7.3 1.9,9.5 3,5.9 0,3.6 3.8,3.6"/>
          <polygon transform="translate(22 0)" points="5,0 6.2,3.6 10,3.6 7,5.9 8.1,9.5 5,7.3 1.9,9.5 3,5.9 0,3.6 3.8,3.6"/>
          <polygon transform="translate(33 0)" points="5,0 6.2,3.6 10,3.6 7,5.9 8.1,9.5 5,7.3 1.9,9.5 3,5.9 0,3.6 3.8,3.6"/>
          <polygon transform="translate(44 0)" points="5,0 6.2,3.6 10,3.6 7,5.9 8.1,9.5 5,7.3 1.9,9.5 3,5.9 0,3.6 3.8,3.6"/>
        </g>
      </svg>
      <b>5.0</b>
    </div>

    <blockquote class="quote-card" style="left:122px">
      <div class="avatar" role="img" aria-label="Portrait photo of the client"></div>
      <p>"Etiam vulputate varius ex in eleifend. Phasellus condimentum diam metus, efficitur ornare risus facilisis a. Nunc eget pharetra turpis, at ornare mi. Nunc venenatis diam mi, ut suscipit nisl imperdiet ut."</p>
      <span class="author">- MARCUS T – Chief Executive Officer -</span>
    </blockquote>
    <blockquote class="quote-card" style="left:372px">
      <div class="avatar" role="img" aria-label="Portrait photo of the client"></div>
      <p>"Etiam vulputate varius ex in eleifend. Phasellus condimentum diam metus, efficitur ornare risus facilisis a. Nunc eget pharetra turpis, at ornare mi. Nunc venenatis diam mi, ut suscipit nisl imperdiet ut."</p>
      <span class="author">- MARCUS T – Chief Executive Officer -</span>
    </blockquote>
    <div class="dots"><span></span><span></span><span class="on"></span><span></span><span></span></div>
  </section>

  <section class="partners">
    <h2>OUR PARTNERS</h2>
    <div class="partner-row">
      <span>Northvale</span>
      <span>leafmark</span>
      <span>Stonegate</span>
      <span>orsen</span>
      <span>Brightpath</span>
    </div>
  </section>

  <footer class="site-footer">
    <div class="footer-col" style="left:122px">
      <h4>More Links</h4>
      <div class="footer-links">
        <span>Home</span><span>Terms of Use</span>
        <span>About Us</span><span>Community</span>
        <span>Products</span><span>Consulting</span>
        <span>Solutions</span><span>Contact</span>
        <span>Contact Us</span><span>Privacy Policy</span>
      </div>
    </div>
    <div class="divider" style="left:220px"></div>
    <div class="footer-col" style="left:240px">
      <h4>Social Media</h4>
      <ul class="footer-social">
        <li><span></span>Like us on Friendfold</li>
        <li><span></span>Follow Us on Chirpline</li>
        <li><span></span>Reelcast Channel</li>
        <li><span></span>Follow us on Workweave</li>
      </ul>
    </div>
    <div class="divider" style="left:329px"></div>
    <div class="footer-col" style="left:349px">
      <h4>Latest News</h4>
      <div class="news">
        <h5>Lorem ipsum dolor sit amet, consectetur</h5>
        <p>adipiscing elit. Donec vestibulum commodo nisl, sit amet commodo orci.</p>
        <h5>Lorem ipsum dolor sit amet, consectetur</h5>
        <p>adipiscing elit. Donec vestibulum commodo nisl, sit amet commodo orci.</p>
      </div>
    </div>
    <div class="divider" style="left:502px"></div>
    <div class="footer-brand">
      <div class="brand-name">harbin</div>
      <div class="brand-sub">BLUE TORCH</div>
      <small>Copyright © 2014 Kestrel Studio.<br>All rights reserved.</small>
    </div>
  </footer>

</div>
</body>
</html>
```